Professional "Aviation Parts" Auction Website with Customer Login Backend Module

Need an "Aviation Parts" Website with 4 major listing options.
- AUCTION
Seller can list their items on the site as an auction with a small listing fee. Seller has to create an account in order to be able to create or edit a listing. Seller must be able to have a reserve price.
- SELLING
Sellers can list their items with a small listing fee. Imortant is, that Sellers has a back end module, (like trovix) where they can log in and create or make changes to existing listings.
- BUYING
Buyers can search items either by part number in a search bar, or scroll through categories and subcategories to find the respective part.
- WANTED
Customers should be able to create a “Wanted” listing for items of interest.

In all four cases, customers (Buyers/Seller) must create an account to either place a bid, buy now, create a “wanted” listing or create/edit their own for sale/auction listing. NO login is required to search the website or browse through categories and to see listings. The website should be “Trovix like” with login module, payment, coindrop connection, etc and easy to navigate. A design example is https://www.quellmarket-hub.com/ . I’m open for all ideas.

Target Market(s)

Aviation Industry
Helicopter Industry

Industry/Entity Type

Aviation

Number of Pages Required

5+ page

Font styles to use
Serif
Sans Serif

Colors
85acd3
3176b5
9d9d9d
d3d3d3

Requirements
Must have
• Our company is called Brelvox.com, LLC and is specialized in aviation parts listings. The website must have 4 major options: Auction, Sell, Buy, and Wanted listings. The Buyer/Seller must create an account in order to bid, buy or sell an item. No login is required if someone just wants to browse the website to look for pricing and parts. Once they decide to purchase, they have to login or create an account. The same counts for the seller. Seller must create an account to list a "For Sale", "Auction" or "Wanted" Listing. Each listing requires a small listing fee, which will be charged by us and should be paid via CoinDrop. CoinDrop should be interfaced as a preferred payment method. Other payment options are available as well. The website idea is very similar to Trovix. Same style listings as Trovix and other auction pages. A good design idea is https://www.quellmarket-hub.com/ to get a better understanding. The website must be easy to navigate and modern looking with a professional color scheme. The logo is attached. I would like to keep the website in a similar color scheme as the logo design.
• There should be two main Categories on the main page to select from:
• - Helicopter Listings
• - Airplane Listings
• The 1st "Sub-Category" once you click on either one of the top category, will be "Aircraft Make".
• The 2nd "Sub-Category" will be "Aircraft Model".
• The 3rd "Sub-Category" will be "Parts" for that specific aircraft.
• Also there should be a CoinDrop interface, if a buyer wants to purchase an item, so they can use their credit card or request wire information from the seller after closing.
• It also has to include an option when a seller lists an item, they will be required to make a payment to us for listing on our website. For example $1.99 for a listing value up to $100. A listing fee for a sale value of up to $1,000 will be $4.99, and so on. Listing fee for up to $10,000 will be $14.99. Listing fee for up to $100.000 will be $49.99. This system is very similar to the Trovix platform.
Nice to have
• It would be nice to have a easy to maintain back-end module which can easily be manged by our personnel.
Should not have
• The page should not look childish with random colors. A professional appearance and easy to navigate is a must.

```html
<!DOCTYPE html>
<html lang="en">
<head>
<meta charset="utf-8">
<title>Brelvox — Aviation Parts</title>
<link href="https://fonts.googleapis.com/css2?family=Montserrat:wght@400;500;600&display=swap" rel="stylesheet">
<style>
:root{
  --blue:#3176b5;
  --blue-light:#85acd3;
  --grey:#9d9d9d;
  --grey-light:#d3d3d3;
  --text:#444;
  --panel:#f3f3f3;
  --footer:#f4f4f4;
  --white:#fff;
  --star:#f5b301;
}
*{box-sizing:border-box;margin:0;padding:0}
html,body{width:748px;height:1200px;overflow:hidden;background:var(--white);font-family:'Montserrat',sans-serif;color:var(--text)}
.page{position:relative;width:748px;height:1200px}
.abs{position:absolute}

/* header */
.site-header{position:absolute;left:0;top:0;width:748px;height:82px;background:var(--white)}
.brand{left:70px;top:31px;display:flex;align-items:center;gap:6px;color:var(--blue);font-size:14px;font-weight:500;letter-spacing:.5px}
.brand-mark{width:10px;height:10px;background:var(--blue)}
.nav a{position:absolute;top:34px;font-size:11px;color:var(--grey);text-decoration:none}
.nav .login{color:var(--blue)}
.nav .sep{position:absolute;left:523px;top:33px;color:var(--blue);font-size:11px}
.nav .active-bar{position:absolute;left:255px;top:80px;width:48px;height:2px;background:var(--blue)}
.btn-create{left:541px;top:29px;width:79px;height:24px;border-radius:3px;background:var(--blue);color:var(--white);font-size:7px;display:flex;align-items:center;justify-content:center}
.cart-badge{left:650px;top:30px;width:8px;height:8px;border-radius:50%;background:var(--blue);color:var(--white);font-size:5px;display:flex;align-items:center;justify-content:center}

/* hero */
.hero{left:0;top:82px;width:748px;height:338px;background:linear-gradient(180deg,#3a3836 0%,#5a4a3e 35%,#9a6440 55%,#4a3a30 75%,#232222 100%)}
.hero-title{left:0;top:152px;width:748px;text-align:center;color:var(--white);font-size:27px;font-weight:500}
.hero-sub{left:0;top:204px;width:748px;text-align:center;color:var(--white);font-size:16px}
.search{left:158px;top:261px;width:433px;height:30px;display:flex;background:var(--white);border-radius:3px;overflow:hidden}
.search .cat{width:61px;border-right:1px solid var(--grey-light);display:flex;align-items:center;padding-left:14px;gap:8px;font-size:11px;color:#333}
.search .field{flex:1;display:flex;align-items:center;padding-left:15px;font-size:10px;color:#555}
.search .go{width:85px;background:var(--blue);color:var(--white);font-size:11px;letter-spacing:.5px;display:flex;align-items:center;justify-content:center}

/* listings */
.section-title{left:61px;font-size:17px;color:var(--blue);font-weight:400}
.pager{display:flex;gap:4px}
.pager span{width:17px;height:17px;border-radius:50%;background:var(--blue);display:flex;align-items:center;justify-content:center}
.card{width:306px;height:166px;background:var(--panel);border-radius:3px}
.card .thumb{position:absolute;left:10px;top:11px;width:132px;height:144px;background:var(--white);box-shadow:0 0 3px rgba(0,0,0,.15);display:flex;align-items:center;justify-content:center}
.thumb .switch{width:83px;height:127px;border-radius:6px;background:linear-gradient(160deg,#2b2b2b,#111)}
.thumb .fan{width:100px;height:110px;border-radius:8px;background:radial-gradient(circle at 40% 55%,#6b6660 0,#b7ab84 35%,#ddd3aa 60%,#f6f3ea 80%)}
.card .info{position:absolute;left:157px;top:24px;width:145px}
.info .name{font-size:12.5px;color:var(--blue);line-height:17px;font-weight:400}
.info .price{font-size:16px;color:#333;margin-top:12px}
.info .meta{font-size:8px;color:var(--grey);margin-top:10px;line-height:16px}
.info .meta.cond{font-weight:500}
.stars{display:flex;gap:4px;margin-top:9px}
.featured .price{margin-top:9px}

/* signup band */
.signup{left:0;top:925px;width:748px;height:165px;background:linear-gradient(120deg,#5f86ab 0%,#3f6f9d 45%,#6990b5 100%)}
.signup .bubble{position:absolute;width:78px;height:78px;border-radius:50%;background:rgba(49,118,181,.75);display:flex;align-items:center;justify-content:center}
.signup .label{position:absolute;top:119px;color:var(--white);font-size:11.5px;font-weight:500;text-align:center;width:200px}

/* footer */
.site-footer{left:0;top:1090px;width:748px;height:110px;background:var(--footer)}
.foot-col h4{font-size:9.5px;font-weight:500;color:#555;margin-bottom:9px}
.foot-col a{display:block;font-size:8px;color:var(--grey);text-decoration:none;margin-bottom:9px;letter-spacing:.3px}
.pay{display:flex;gap:6px}
.pay span{width:40px;height:25px;background:var(--white);border:1px solid var(--grey-light);border-radius:3px;font-size:7px;color:var(--blue);font-weight:600;display:flex;align-items:center;justify-content:center}
.copyright{left:400px;top:77px;width:286px;text-align:right;font-size:8px;color:var(--grey);letter-spacing:.3px}
</style>
</head>
<body>
<div class="page">

  <header class="site-header">
    <div class="abs brand"><span class="brand-mark"></span>BRELVOX</div>
    <nav class="nav">
      <a href="#" style="left:262px">Home</a>
      <a href="#" style="left:317px">Who we are</a>
      <a href="#" style="left:401px">Sell</a>
      <a href="#" style="left:442px">Buy</a>
      <a href="#" class="login" style="left:482px">Loign</a>
      <span class="sep">|</span>
      <span class="active-bar"></span>
    </nav>
    <div class="abs btn-create">Create an account</div>
    <svg class="abs" style="left:638px;top:33px" width="16" height="16" viewBox="0 0 16 16" fill="none" stroke="#3176b5" stroke-width="1.5">
      <path d="M1 2h2.5l2 8h7l1.5-6H4.5"/><circle cx="6.5" cy="13.5" r="1.2"/><circle cx="12" cy="13.5" r="1.2"/>
    </svg>
    <div class="abs cart-badge">1</div>
    <svg class="abs" style="left:671px;top:34px" width="15" height="14" viewBox="0 0 24 22" fill="none" stroke="#3176b5" stroke-width="2.4">
      <path d="M12 20S2 13.5 2 7.5A5 5 0 0 1 12 5a5 5 0 0 1 10 2.5C22 13.5 12 20 12 20z"/>
    </svg>
  </header>

  <section class="abs hero" role="img" aria-label="Business jet parked on a runway at sunset, with a scroll-down doodle"></section>
  <h1 class="abs hero-title">BRELVOX</h1>
  <p class="abs hero-sub">Your one stop shop for aviation parts</p>
  <div class="abs search">
    <div class="cat">All
      <svg width="10" height="6" viewBox="0 0 10 6" fill="none" stroke="#333" stroke-width="1"><path d="M1 1l4 4 4-4"/></svg>
    </div>
    <div class="field">What are you looking for ?</div>
    <div class="go">SEARCH</div>
  </div>

  <!-- Recent listings -->
  <h2 class="abs section-title" style="top:444px">Recent Listings</h2>
  <div class="abs pager" style="left:648px;top:448px">
    <span><svg width="7" height="8" viewBox="0 0 7 8" fill="none" stroke="#fff" stroke-width="1.3"><path d="M5 1L2 4l3 3"/></svg></span>
    <span><svg width="7" height="8" viewBox="0 0 7 8" fill="none" stroke="#fff" stroke-width="1.3"><path d="M2 1l3 3-3 3"/></svg></span>
  </div>

  <article class="abs card" style="left:60px;top:487px">
    <div class="thumb"><div class="switch" role="img" aria-label="Emergency locator transmitter remote switch panel"></div></div>
    <div class="info">
      <h3 class="name">KESTREL - REMOTE SWITCH FOR KE406</h3>
      <div class="price">$749.95</div>
      <div class="meta">6 Bids<br>9d 16h left (5/18, 12PM)</div>
    </div>
  </article>
  <article class="abs card" style="left:380px;top:487px">
    <div class="thumb"><div class="fan" role="img" aria-label="Condenser blower assembly"></div></div>
    <div class="info">
      <h3 class="name">CONDENSER BLOWER ASSEMBLY</h3>
      <div class="price">$749.95</div>
      <div class="meta cond">Condition : New</div>
    </div>
  </article>

  <!-- Featured listings -->
  <h2 class="abs section-title" style="top:675px">Featured Listings</h2>
  <div class="abs pager" style="left:648px;top:679px">
    <span><svg width="7" height="8" viewBox="0 0 7 8" fill="none" stroke="#fff" stroke-width="1.3"><path d="M5 1L2 4l3 3"/></svg></span>
    <span><svg width="7" height="8" viewBox="0 0 7 8" fill="none" stroke="#fff" stroke-width="1.3"><path d="M2 1l3 3-3 3"/></svg></span>
  </div>

  <article class="abs card featured" style="left:60px;top:718px">
    <div class="thumb"><div class="switch" role="img" aria-label="Emergency locator transmitter remote switch panel"></div></div>
    <div class="info">
      <h3 class="name">KESTREL - REMOTE SWITCH FOR KE406</h3>
      <div class="stars">
        <svg width="10" height="10" viewBox="0 0 10 10"><path d="M5 0l1.5 3.3 3.5.3-2.7 2.3.9 3.5L5 7.5 1.8 9.4l.9-3.5L0 3.6l3.5-.3z" fill="#f5b301"/></svg>
        <svg width="10" height="10" viewBox="0 0 10 10"><path d="M5 0l1.5 3.3 3.5.3-2.7 2.3.9 3.5L5 7.5 1.8 9.4l.9-3.5L0 3.6l3.5-.3z" fill="#f5b301"/></svg>
        <svg width="10" height="10" viewBox="0 0 10 10"><path d="M5 0l1.5 3.3 3.5.3-2.7 2.3.9 3.5L5 7.5 1.8 9.4l.9-3.5L0 3.6l3.5-.3z" fill="#f5b301"/></svg>
        <svg width="10" height="10" viewBox="0 0 10 10"><path d="M5 0l1.5 3.3 3.5.3-2.7 2.3.9 3.5L5 7.5 1.8 9.4l.9-3.5L0 3.6l3.5-.3z" fill="#f5b301"/></svg>
        <svg width="10" height="10" viewBox="0 0 10 10"><path d="M5 0l1.5 3.3 3.5.3-2.7 2.3.9 3.5L5 7.5 1.8 9.4l.9-3.5L0 3.6l3.5-.3z" fill="#d3d3d3"/></svg>
      </div>
      <div class="price">$749.95</div>
      <div class="meta">6 Bids<br>9d 16h left (5/18, 12PM)</div>
    </div>
  </article>
  <article class="abs card featured" style="left:380px;top:718px">
    <div class="thumb"><div class="fan" role="img" aria-label="Condenser blower assembly"></div></div>
    <div class="info">
      <h3 class="name">CONDENSER BLOWER ASSEMBLY</h3>
      <div class="stars">
        <svg width="10" height="10" viewBox="0 0 10 10"><path d="M5 0l1.5 3.3 3.5.3-2.7 2.3.9 3.5L5 7.5 1.8 9.4l.9-3.5L0 3.6l3.5-.3z" fill="#f5b301"/></svg>
        <svg width="10" height="10" viewBox="0 0 10 10"><path d="M5 0l1.5 3.3 3.5.3-2.7 2.3.9 3.5L5 7.5 1.8 9.4l.9-3.5L0 3.6l3.5-.3z" fill="#f5b301"/></svg>
        <svg width="10" height="10" viewBox="0 0 10 10"><path d="M5 0l1.5 3.3 3.5.3-2.7 2.3.9 3.5L5 7.5 1.8 9.4l.9-3.5L0 3.6l3.5-.3z" fill="#f5b301"/></svg>
        <svg width="10" height="10" viewBox="0 0 10 10"><path d="M5 0l1.5 3.3 3.5.3-2.7 2.3.9 3.5L5 7.5 1.8 9.4l.9-3.5L0 3.6l3.5-.3z" fill="#f5b301"/></svg>
        <svg width="10" height="10" viewBox="0 0 10 10"><path d="M5 0l1.5 3.3 3.5.3-2.7 2.3.9 3.5L5 7.5 1.8 9.4l.9-3.5L0 3.6l3.5-.3z" fill="#d3d3d3"/></svg>
      </div>
      <div class="price">$749.95</div>
      <div class="meta cond">Condition : New</div>
    </div>
  </article>

  <!-- Sign up band -->
  <section class="abs signup" role="img" aria-label="Airliner in flight against a blue sky">
    <div class="bubble" style="left:228px;top:22px">
      <svg width="28" height="30" viewBox="0 0 28 30" fill="none" stroke="#fff" stroke-width="1.6">
        <path d="M9 2h10l-3 6h-4z"/><path d="M12 8C4 12 2 20 3 24c1 3 4 4 11 4s10-1 11-4c1-4-1-12-9-16"/>
        <path d="M17 15.5c-1-1-5-1.5-5 1s5 1.5 5 4-4 2.5-5 1M14.5 13v2M14.5 22.5v2"/>
      </svg>
    </div>
    <div class="bubble" style="left:444px;top:22px">
      <svg width="32" height="30" viewBox="0 0 32 30" fill="none" stroke="#fff" stroke-width="1.8">
        <path d="M1 3h5l3 15h19l3-11H8"/><circle cx="12" cy="25" r="2.2" fill="#fff"/><circle cx="25" cy="25" r="2.2" fill="#fff"/>
      </svg>
    </div>
    <div class="label" style="left:167px">SIGN UP AS A SELLER</div>
    <div class="label" style="left:384px">SIGN UP AS A BUYER</div>
  </section>

  <!-- Footer -->
  <footer class="abs site-footer">
    <div class="abs foot-col" style="left:62px;top:18px">
      <h4>THE COMPANY</h4>
      <a href="#">ABOUT US</a><a href="#">WHAT WE OFFER</a><a href="#">TERMS OF SERVICE</a>
    </div>
    <div class="abs foot-col" style="left:257px;top:18px">
      <h4>LET US HELP YOU</h4>
      <a href="#">YOUR ORDERS</a><a href="#">SUPPORT</a><a href="#">FAQ</a>
    </div>
    <div class="abs pay" style="left:513px;top:32px">
      <span>Veyra</span><span>Mondacard</span><span>CoinDrop</span><span>Amplex</span>
    </div>
    <div class="abs copyright">© BRELVOX. ALL RIGHTS RESERVED 2018</div>
  </footer>

</div>
</body>
</html>
```